Stationery and Business Cards
PulseHaven
Bright & Fun-filled
Tessa Lund
Massage Therapist
42 Caxbury Vale Road
London
e4 8QT
massage@pulsehaven.co.uk
www.pulsehaven.co.uk

```html
<!DOCTYPE html>
<html lang="en">
<head>
<meta charset="utf-8">
<title>PulseHaven Business Cards</title>
<link rel="stylesheet" href="https://fonts.googleapis.com/css2?family=Nunito+Sans:wght@400;700;800&display=swap">
<style>
  :root {
    --backdrop: #e9ebee;
    --navy: #1c3b59;
    --navy-deep: #16304a;
    --green: #5fb78a;
    --paper: #ffffff;
    --ink: #2b3a48;
    --muted: #6b7884;
    --rule: #5fb78a;
  }
  * { box-sizing: border-box; margin: 0; padding: 0; }
  html, body {
    width: 1200px; height: 874px; overflow: hidden;
    background: var(--backdrop);
    font-family: "Nunito Sans", Arial, sans-serif;
  }
  .stationery {
    width: 1200px; height: 874px;
    display: flex; align-items: center; justify-content: center; gap: 60px;
  }
  .card {
    width: 520px; height: 336px; position: relative;
    box-shadow: 0 10px 30px rgba(20, 40, 60, 0.18);
  }
  .brand { display: flex; align-items: center; }
  .brand-dot { border-radius: 50%; background: var(--green); flex: none; }

  /* Front */
  .card--front { background: linear-gradient(160deg, var(--navy) 0%, var(--navy-deep) 100%); }
  .card--front .brand {
    position: absolute; left: 40px; bottom: 70px; gap: 14px;
  }
  .card--front .brand-dot { width: 18px; height: 18px; }
  .card--front .brand-name {
    color: var(--paper); font-weight: 800; font-size: 54px; letter-spacing: -0.5px; line-height: 1;
  }
  .card--front .tagline {
    position: absolute; left: 72px; bottom: 44px;
    color: var(--green); font-size: 17px; letter-spacing: 1.5px;
  }

  /* Back */
  .card--back { background: var(--paper); }
  .card--back .brand {
    position: absolute; left: 34px; top: 34px; gap: 10px;
  }
  .card--back .brand-dot { width: 12px; height: 12px; }
  .card--back .brand-name {
    color: var(--navy); font-weight: 800; font-size: 32px; line-height: 1; letter-spacing: -0.3px;
  }
  .card--back .tagline {
    position: absolute; left: 56px; top: 74px;
    color: var(--green); font-size: 11px; letter-spacing: 1.2px;
  }
  .header-rule {
    position: absolute; left: 34px; right: 34px; top: 98px;
    height: 2px; background: var(--rule);
  }
  .person { position: absolute; right: 34px; top: 38px; text-align: right; }
  .person-name { color: var(--navy); font-weight: 700; font-size: 18px; }
  .person-role { color: var(--muted); font-size: 12px; margin-top: 2px; }
  .contact {
    position: absolute; left: 34px; top: 132px;
    color: var(--ink); font-size: 13px; line-height: 1.55; font-style: normal;
  }
  .contact-label { color: var(--green); font-weight: 700; margin-right: 4px; }
  .contact-gap { height: 10px; }
  .website {
    position: absolute; left: 34px; bottom: 30px;
    color: var(--navy); font-weight: 700; font-size: 14px; letter-spacing: 0.3px;
  }
</style>
</head>
<body>
  <main class="stationery">
    <section class="card card--front" aria-label="Business card front">
      <div class="brand">
        <span class="brand-dot"></span>
        <span class="brand-name">PulseHaven</span>
      </div>
      <p class="tagline">Unwind, Restore, Revive</p>
    </section>

    <section class="card card--back" aria-label="Business card back">
      <div class="brand">
        <span class="brand-dot"></span>
        <span class="brand-name">PulseHaven</span>
      </div>
      <p class="tagline">Unwind, Restore, Revive</p>
      <div class="person">
        <p class="person-name">Tessa Lund</p>
        <p class="person-role">Massage Therapist</p>
      </div>
      <div class="header-rule"></div>
      <address class="contact">
        <p>42 Caxbury Vale Road</p>
        <p>London, e4 8QT</p>
        <div class="contact-gap"></div>
        <p><span class="contact-label">T:</span>07700 900417</p>
        <p><span class="contact-label">E:</span>massage@pulsehaven.co.uk</p>
      </address>
      <p class="website">www.pulsehaven.co.uk</p>
    </section>
  </main>
</body>
</html>
```